Bold Modern Creative Wine Label Needed for a Chardonnay

We need a modern, eye catching label, one that will appeal to millennials, but also attract the older more conservative crowd. We like the boldness of black on white but are open to your suggestions. Since the bottle type is a light green 'burgundy style' bottle, you should take that into account. The name of the brand is Ko`. The attached label is example of what we like very much. It is eye catching and bold and modern. Keep in mind that the bottle will be light green in color so black and white might not work so well. Use your creativity please! The label can be any size but needs to fit on this shape bottle. See attached photos. thanks!!

(Please no grapes or wine glasses or wine bottles featured on the label!)

Hi Designers, I just wanted to let you know that we received many great designs and we are sorting through them this week. The website is making it a bit difficult to create a 'poll' so this is taking longer than we expected. Thanks for all the great submissions!

```html
<!DOCTYPE html>
<html lang="en">
<head>
<meta charset="utf-8">
<title>Ko Winery — Chardonnay Label Series</title>
<link rel="stylesheet" href="https://fonts.googleapis.com/css2?family=Libre+Baskerville:ital,wght@0,400;0,700;1,400&family=Open+Sans:wght@300&display=swap">
<style>
  :root {
    --page: #ffffff;
    --ink-black: #1e1e1e;
    --ink-black-edge: #2b2b2b;
    --gold: #c9a646;
    --gold-line: #d8b24e;
    --paper-white: #f1f1f1;
    --paper-cream: #f4efc4;
    --wine: #a0243a;
    --berry: #8c1f4a;
    --olive: #7b7a2c;
    --text-dark: #2a2a2a;
    --numeral: #8a8a8a;
    --vine-green: #c8d35a;
  }
  * { margin: 0; padding: 0; box-sizing: border-box; }
  html, body { width: 1200px; height: 764px; overflow: hidden; background: var(--page); }
  .series { position: relative; width: 1200px; height: 764px; }
  .label {
    position: absolute;
    display: flex; flex-direction: column; align-items: center; justify-content: center;
    text-align: center;
    font-family: "Libre Baskerville", Georgia, serif;
  }
  .label--black { background: var(--ink-black); color: var(--gold); }
  .label--white { background: var(--paper-white); color: var(--text-dark); }
  .label--cream { background: var(--paper-cream); color: var(--text-dark); }
  .label--banded { border-top: 2px solid var(--gold-line); border-bottom: 2px solid var(--gold-line); outline: 4px solid var(--ink-black); }
  .brand-name { font-weight: 400; line-height: 1; letter-spacing: 1px; }
  .tagline { font-style: italic; font-size: 10px; margin-top: 6px; }
  .since { font-weight: 700; font-size: 7.5px; margin-top: 6px; letter-spacing: .3px; }
  .volume { font-size: 6px; margin-top: 5px; }
  .volume--bold { font-weight: 700; font-size: 7.5px; }
  .vineyard-art { width: 90px; height: 62px; display: block; }
  .maker { font-size: 8px; margin-top: 2px; }
  .numeral {
    position: absolute; top: 695px; width: 40px; text-align: center;
    font-family: "Open Sans", Arial, sans-serif; font-weight: 300; font-size: 30px; color: var(--numeral);
  }
</style>
</head>
<body>
<main class="series">

  <section class="label label--black label--banded" style="left:27px; top:404px; width:168px; height:162px;">
    <div class="brand-name" style="font-size:44px;">Ko</div>
    <p class="tagline">A blended wine just for U</p>
    <p class="since">SINCE 2009</p>
    <p class="volume">12% ALC VOL 750ml</p>
  </section>

  <section class="label label--white" style="left:220px; top:328px; width:170px; height:126px;">
    <div class="brand-name" style="font-size:36px; color:var(--berry);">Ko</div>
    <p class="tagline" style="font-size:8.5px;">A blended wine just for U</p>
    <p class="since" style="color:var(--wine);">SINCE 2009</p>
    <p class="volume volume--bold">12% ALC VOL 750ml</p>
  </section>

  <section class="label label--cream" style="left:419px; top:318px; width:160px; height:138px;">
    <div class="brand-name" style="font-size:36px; color:var(--wine);">Ko</div>
    <p class="tagline" style="color:var(--wine); font-size:9px;">A blended wine just for U</p>
    <p class="since">SINCE 2009</p>
    <p class="volume">12% ALC VOL 750ml</p>
  </section>

  <section class="label label--cream" style="left:607px; top:423px; width:172px; height:172px;">
    <div class="brand-name" style="font-size:44px; color:var(--wine);">Ko</div>
    <p class="tagline" style="color:var(--wine);">A blended wine just for U</p>
    <p class="since">SINCE 2009</p>
    <p class="volume">12% ALC VOL 750ml</p>
  </section>

  <section class="label label--white" style="left:797px; top:388px; width:166px; height:162px;">
    <svg class="vineyard-art" role="img" aria-label="Illustration of two children reaching up toward a hanging bunch of grapes" viewBox="0 0 90 62">
      <rect x="0" y="0" width="90" height="62" fill="var(--paper-white)"/>
      <circle cx="60" cy="14" r="11" fill="var(--vine-green)" opacity=".7"/>
      <rect x="30" y="36" width="32" height="22" rx="4" fill="var(--ink-black)" opacity=".25"/>
    </svg>
    <div class="brand-name" style="font-size:28px; color:var(--ink-black);">Ko</div>
    <p class="maker">By Ko Winery</p>
    <p class="since" style="font-weight:400;">SINCE 2009</p>
    <p class="volume volume--bold" style="font-weight:400;">12% ALC VOL 750ml</p>
  </section>

  <section class="label label--black" style="left:987px; top:353px; width:170px; height:140px; border:1px solid var(--ink-black-edge);">
    <div class="brand-name" style="font-size:40px;">Ko</div>
    <p class="tagline">A blended wine just for U</p>
    <p class="since">SINCE 2009</p>
    <p class="volume">12% ALC VOL 750ml</p>
  </section>

  <span class="numeral" style="left:92px;">1</span>
  <span class="numeral" style="left:272px;">2</span>
  <span class="numeral" style="left:474px;">3</span>
  <span class="numeral" style="left:673px;">4</span>
  <span class="numeral" style="left:866px;">5</span>
  <span class="numeral" style="left:1052px;">6</span>

</main>
</body>
</html>
```